Home Health Company Needs a Corporate Identity Package

We need a corporate identity package (see what it should include below) for a home health care company. The design should be professional, uncluttered, simple and created in Publisher (so that we can edit the design in the future, if necessary. )
We need the following created:
-Presentation folder
-Business card template (color, double sided)
-Letterhead
-Stationary
-postcard sized marketing piece (5.5" x 8.5", color, double sided)

Target Market(s)

We are in the business of supplying personal care aids for in home care. Our services are directed towards older, retired individuals with some disability or illness. However, we will be marketing to the children or relatives of our in home clients. We want our logo to emphasize our reliability and personalized services.

Industry/Entity Type

Home Health Care

Requirements
Must have
• The design should be professional, uncluttered, simple and created in Publisher (so that we can edit the design in the future, if necessary. )

```html
<!DOCTYPE html>
<html lang="en">
<head>
<meta charset="utf-8">
<title>Evenfield Home Health – Business Card</title>
<link rel="stylesheet" href="https://fonts.googleapis.com/css2?family=Arimo:ital,wght@0,400;0,700;1,700&family=Roboto+Condensed:wght@700&display=swap">
<style>
  :root {
    --bg: #e9ebee;
    --card-dark: #2c2a2b;
    --card-light: #ffffff;
    --brand-blue: #4bb6d4;
    --text-grey: #5f5f5f;
    --rule: #3a3a3a;
  }
  * { box-sizing: border-box; margin: 0; padding: 0; }
  html, body {
    width: 1200px;
    height: 784px;
    overflow: hidden;
    background: var(--bg);
  }
  .sheet {
    width: 1200px;
    height: 784px;
    display: flex;
    align-items: center;
    justify-content: center;
    gap: 40px;
  }
  .card {
    width: 540px;
    height: 309px;
    border-radius: 4px;
    box-shadow: 0 6px 18px rgba(0,0,0,0.18);
    position: relative;
    overflow: hidden;
  }

  /* Front side */
  .card--front {
    background: var(--card-dark);
    display: flex;
    align-items: center;
    justify-content: center;
  }
  .brand {
    display: flex;
    align-items: center;
    gap: 18px;
    font-family: "Roboto Condensed", "Arial Narrow", sans-serif;
    font-weight: 700;
    color: var(--brand-blue);
  }
  .brand__dot {
    width: 56px;
    height: 56px;
    border-radius: 50%;
    background: var(--brand-blue);
    flex: none;
  }
  .brand__name {
    font-size: 46px;
    line-height: 0.95;
    letter-spacing: 0.5px;
  }
  .brand--small { gap: 10px; }
  .brand--small .brand__dot { width: 26px; height: 26px; }
  .brand--small .brand__name { font-size: 20px; }

  /* Back side */
  .card--back {
    background: var(--card-light);
    padding: 30px 36px;
    font-family: "Arimo", Arial, sans-serif;
    color: var(--text-grey);
  }
  .card--back .brand { margin-bottom: 34px; }
  .holder__name {
    font-size: 27px;
    font-weight: 400;
    line-height: 1.1;
  }
  .holder__role {
    font-size: 17px;
    font-weight: 700;
    font-style: italic;
    margin-bottom: 18px;
  }
  .contact {
    display: flex;
    gap: 34px;
    font-size: 15px;
    line-height: 1.35;
  }
  .contact__group { list-style: none; }
  .card__rule {
    position: absolute;
    top: 30px;
    bottom: 30px;
    right: 44px;
    width: 2px;
    background: var(--rule);
  }
</style>
</head>
<body>
  <main class="sheet">
    <section class="card card--back" aria-label="Business card, contact side">
      <div class="brand brand--small">
        <span class="brand__dot"></span>
        <span class="brand__name">Evenfield Home Health</span>
      </div>
      <p class="holder__name">Your Name</p>
      <p class="holder__role">Position</p>
      <div class="contact">
        <ul class="contact__group">
          <li>Address: xxxxxxxxxx</li>
          <li>xxxxxxxxxxxxxxxx</li>
          <li>Phone: xxxxxxxxx</li>
        </ul>
        <ul class="contact__group">
          <li>Fax:xxxxxxxxxx</li>
          <li>Email: xxxxxxxx</li>
          <li>Web: xxxxxxxxx</li>
        </ul>
      </div>
      <span class="card__rule"></span>
    </section>

    <section class="card card--front" aria-label="Business card, brand side">
      <div class="brand">
        <span class="brand__dot"></span>
        <span class="brand__name">Evenfield<br>Home Health</span>
      </div>
    </section>
  </main>
</body>
</html>
```